New design for weblog: joostvanleer.nl

My name is Joost van Leer, I am a tv presenter / radio-dj / writer from The Netherlands. I would like you to make a fresh new design for my weblog http://www.joostvanleer.nl. Please give it a 2010 look, with new colors and layout. Be creative, have fun!

Target Market(s)

- Fans and visitors of my blog
- Current and future employers

Number of Pages Required

1 page

Requirements
Must have
• - Must use my new "joostvanleer.nl" logo (as provided) 
Nice to have
• - Use the picture(s) i uploaded
Should not have
• x

```html
<!DOCTYPE html>
<html lang="en">
<head>
<meta charset="utf-8">
<title>joostvanleer.nl</title>
<link rel="stylesheet" href="https://fonts.googleapis.com/css2?family=Arimo:wght@400;700&family=Tinos:wght@400;700&display=swap">
<style>
:root{
  --bg:#e3978a;
  --page:#ece8da;
  --purple:#3e3a63;
  --purple-soft:#4a4575;
  --beige:#e4e0cd;
  --panel:#ffffff;
  --line:#cfcabb;
  --link:#7b2a5e;
  --text:#333333;
  --accent:#4da3d8;
  --salmon:#e3978a;
}
*{box-sizing:border-box;margin:0;padding:0}
html,body{width:1139px;height:1200px;overflow:hidden}
body{background:var(--bg);font-family:"Arimo",Arial,sans-serif;color:var(--text);font-size:12px;position:relative}
.page{position:absolute;left:92px;top:10px;width:961px;height:1180px;background:var(--page)}
.abs{position:absolute}
.topbar{left:10px;top:0;width:941px;height:29px;background:var(--purple);color:#fff;font-size:11px;font-weight:700;display:flex;align-items:center;justify-content:space-between;padding:0 14px}
.topbar .feeds{display:flex;gap:18px}
.topbar .feeds span::before{content:"";display:inline-block;width:12px;height:12px;background:#f08a24;border-radius:2px;margin-right:6px;vertical-align:-2px}
.masthead{left:10px;top:29px;width:941px;height:98px;background:var(--purple-soft)}
.masthead .portrait{position:absolute;left:0;top:0;width:304px;height:98px;background:linear-gradient(90deg,#d7785a,#b35a4a 40%,#6a4b4f)}
.brand{position:absolute;left:4px;top:6px;display:flex;align-items:center;gap:5px;font-size:10px;color:#fff;font-weight:700}
.brand i{width:10px;height:10px;background:var(--accent);display:block}
.masthead .banner{position:absolute;left:457px;top:16px;width:468px;height:66px;background:var(--salmon);border:4px solid var(--accent)}
.nav{left:10px;top:131px;width:941px;height:35px;background:var(--beige);font-family:"Tinos",Georgia,serif;font-size:17px;display:flex;align-items:center;padding:0 14px;gap:26px;color:#222}
.search{position:absolute;right:12px;top:4px;display:flex;gap:8px}
.search span{width:224px;height:24px;background:#fff;border:1px solid #b9b4a3;font-family:"Arimo",sans-serif;font-size:11px;color:#666;padding:4px 6px}
.btn{background:var(--purple);color:#fff;font-family:"Arimo",sans-serif;font-size:11px;font-weight:700;padding:5px 7px;border:1px solid #222}
.subnav{left:10px;top:168px;width:941px;height:18px;background:var(--purple);color:#fff;font-size:10px;font-weight:700;display:flex;align-items:center;gap:30px;padding:0 12px}
.panel{position:absolute;background:var(--panel);border:1px solid var(--line);padding:8px 10px}
.panel h3{background:var(--purple);color:#fff;font-size:10px;font-weight:700;text-transform:uppercase;padding:5px 8px;margin-bottom:10px}
.panel a,.link{color:var(--link);text-decoration:none}
.panel ul{list-style:none}
.panel li{font-size:11px;margin-bottom:8px;display:flex;align-items:center;gap:6px}
.panel li::before{content:"★";color:#999;font-size:12px}
.featured{left:20px;top:202px;width:600px;height:419px;padding:10px}
.featured .stage{position:absolute;left:10px;top:10px;right:10px;bottom:10px;background:#000}
.featured .tag{position:absolute;right:14px;top:4px;color:#777;font-size:11px}
.featured .photo{position:absolute;left:46px;top:56px;width:490px;height:281px;background:linear-gradient(180deg,#7d7f8e,#b77a6b 55%,#4b3f44)}
.featured .arrow{position:absolute;top:180px;color:#333;font-size:30px}
.featured .cap{position:absolute;left:8px;top:320px;color:#fff;font-family:"Tinos",serif;font-size:16px}
.featured .sub{position:absolute;left:8px;top:342px;color:#ccc;font-size:10px}
.post{margin-bottom:6px}
.post b{display:block;color:var(--link);font-size:11px;margin-bottom:4px}
.post p{font-size:11px}
.divider{border-top:1px dotted #8a7fa6;margin:8px 0}
.more{font-size:11px;font-weight:700;color:var(--link)}
.social{display:flex;gap:56px;padding:8px 0 0 8px}
.social div{display:flex;flex-direction:column;align-items:center;gap:6px;font-size:11px;font-weight:700;color:var(--purple);width:60px}
.social i{display:block;width:58px;height:58px;border-radius:50%;background:#dedbe8}
.enews p{font-size:11px;line-height:1.4;padding-left:46px;position:relative;margin-bottom:10px}
.enews p::before{content:"";position:absolute;left:0;top:0;width:36px;height:36px;background:#e58bb8;border-radius:6px}
.field{width:254px;height:24px;border:1px solid #aaa;background:#f3f1ea;font-size:10px;color:#777;padding:5px}
.footer{left:10px;top:1148px;width:941px;height:28px;background:var(--purple);color:#fff;font-size:9.5px;display:flex;align-items:center;justify-content:center}
</style>
</head>
<body>
<div class="page">
  <div class="abs topbar"><span>Monday, December 21, 2009</span><span class="feeds"><span>NEWS FEED</span><span>COMMENTS</span></span></div>
  <header class="abs masthead">
    <div class="portrait" role="img" aria-label="Portrait photo of Joost van Leer against a red backdrop"></div>
    <div class="brand"><i></i>joostvanleer.nl</div>
    <div class="banner"></div>
  </header>
  <nav class="abs nav"><span>Home</span><span>About</span>
    <div class="search"><span>Search this website...</span><b class="btn">GO</b></div>
  </nav>
  <div class="abs subnav"><span>JOOST'S BLOG</span><span>VIDEOS</span></div>

  <section class="panel featured">
    <div class="stage">
      <span class="tag">Featured Content</span>
      <div class="photo" role="img" aria-label="Team photo of a wheelchair basketball squad in a sports hall"></div>
      <span class="arrow" style="left:6px">‹</span><span class="arrow" style="right:6px">›</span>
      <div class="cap">Sample Post 2</div>
      <div class="sub">Sample post to gallery 2.</div>
    </div>
  </section>

  <section class="panel" style="left:20px;top:631px;width:298px;height:186px">
    <h3>Joost's Blog</h3>
    <div class="post"><b>Sample Post 2</b><p>Sample post to gallery 2. <span class="link">Read More →</span></p></div>
    <div class="divider"></div>
    <div class="post"><b>Sample Post</b><p>Sample Post to gallery <span class="link">Read More →</span></p></div>
    <div class="divider"></div>
    <div class="more">Read More Posts From Joost's Blog</div>
  </section>
  <section class="panel" style="left:324px;top:631px;width:296px;height:186px">
    <h3>Joost's Blog</h3>
    <div class="post"><b>Sample Post 2</b><p>Sample post to gallery 2. <span class="link">Read More →</span></p></div>
    <div class="divider"></div>
    <div class="post"><b>Sample Post</b><p>Sample Post to gallery <span class="link">Read More →</span></p></div>
    <div class="divider"></div>
    <div class="more">Read More Posts From Joost's Blog</div>
  </section>
  <section class="panel" style="left:20px;top:829px;width:600px;height:131px">
    <h3>Videos</h3>
    <div class="post"><b>Hello world!</b><p>Welcome to PressKit. This is your first post. Edit or delete it, then start blogging! <span class="link">Read More →</span></p></div>
    <div class="divider"></div>
    <div class="more">Read More Posts From Videos</div>
  </section>
  <section class="panel" style="left:20px;top:980px;width:600px;height:160px">
    <h3>Connect and network with Joost van Leer</h3>
    <div class="social">
      <div><i></i>Chirpline</div><div><i></i>Friendbook</div><div><i></i>ClipTube</div><div><i></i>CallNet</div><div><i></i>Reelio</div>
    </div>
  </section>

  <aside>
    <section class="panel enews" style="left:627px;top:202px;width:314px;height:160px">
      <h3>Enews &amp; Updates</h3>
      <p>Sign up to receive breaking news<br>as well as receive other site updates!</p>
      <div class="field">Enter your email address...</div>
      <b class="btn" style="display:inline-block;margin-top:6px">GO</b>
    </section>
    <section class="panel" style="left:627px;top:372px;width:314px;height:124px">
      <h3>Recent Posts</h3>
      <ul><li><a>Sample Post 2</a></li><li><a>Sample Post</a></li><li><a>Hello world!</a></li></ul>
    </section>
    <section class="panel" style="left:627px;top:507px;width:165px;height:100px">
      <h3>Categories</h3>
      <ul><li><a>Joost's Blog</a></li><li><a>Videos</a></li></ul>
    </section>
    <section class="panel" style="left:627px;top:621px;width:165px;height:69px">
      <h3>Archives</h3>
      <ul><li><a>December 2009</a></li></ul>
    </section>
    <section class="panel" style="left:802px;top:507px;width:139px;height:210px">
      <h3>Blogroll</h3>
      <ul><li><a>Development Blog</a></li><li><a>Documentation</a></li><li><a>Plugins</a></li><li><a>Suggest Ideas</a></li><li><a>Support Forum</a></li><li><a>Themes</a></li><li><a>PressKit Planet</a></li></ul>
    </section>
    <section class="panel" style="left:802px;top:729px;width:139px;height:143px">
      <h3>Admin</h3>
      <ul><li><a>Site Admin</a></li><li><a>Log out</a></li><li><a>PressKit</a></li><li><a>XHTML</a></li></ul>
    </section>
  </aside>

  <footer class="abs footer">Copyright © 2009 · All Rights Reserved · Dusk Violet Lifestyle Theme by Stroke Studio · Powered by PressKit · Log out</footer>
</div>
</body>
</html>
```